Invitation Design Project

50th Birthday Party for Tim. Big, loud party planned with loads of friends and family. at our home. Decorations will be coloured lanterns attached to the pergola and hired a band.

Details:

on 19th October, 2013
(other details when design chosen)
at: 7.00 pm
RSVP: 14th October, 2013

```html
<!DOCTYPE html>
<html lang="en">
<head>
<meta charset="utf-8">
<title>50th Birthday Party Invitation for Tim</title>
<link href="https://fonts.googleapis.com/css2?family=Pinyon+Script&family=Fredoka:wght@600&family=Open+Sans+Condensed:ital,wght@1,300&family=Indie+Flower&family=Delius&display=swap" rel="stylesheet">
<style>
  :root {
    --page: #ffffff;
    --orange-light: #f6b865;
    --orange: #f2a549;
    --orange-pale: #f9cf92;
    --wine: #c0261f;
    --band-dark: #d9473a;
    --band-light: #ee9660;
    --ink: #111111;
    --white: #ffffff;
    --drink: #c84a3a;
    --glow: #f3d7a6;
  }
  * { margin: 0; padding: 0; box-sizing: border-box; }
  html, body { width: 1200px; height: 1000px; overflow: hidden; background: var(--page); }
  .canvas { position: relative; width: 1200px; height: 1000px; }

  .side-label {
    position: absolute; display: flex; align-items: center; gap: 18px;
    font-family: "Open Sans Condensed", "Arial Narrow", sans-serif;
    font-style: italic; font-weight: 300; font-size: 46px; letter-spacing: 7px; color: var(--ink);
  }
  .side-label--front { left: 145px; top: 52px; }
  .side-label--back { left: 768px; top: 806px; }

  .card { position: absolute; overflow: hidden; background: linear-gradient(180deg, var(--orange-light), var(--orange) 60%, var(--orange-pale)); }
  .card__arc { position: absolute; inset: 0; }

  .card--front { left: 38px; top: 205px; width: 532px; height: 747px; }
  .title { position: absolute; font-family: "Pinyon Script", cursive; color: var(--wine); line-height: 1; }
  .title__age { left: 30px; top: 60px; font-size: 66px; }
  .title__age sup { font-size: 34px; vertical-align: 28px; }
  .title__birthday { left: 78px; top: 108px; font-size: 132px; }
  .title__party { left: 232px; top: 230px; font-size: 92px; }

  .name-band {
    position: absolute; left: 0; top: 328px; width: 100%; height: 65px;
    background: linear-gradient(90deg, var(--band-dark), var(--band-light));
    display: flex; align-items: center; justify-content: center; gap: 12px; color: var(--white);
  }
  .name-band__for { font-family: "Indie Flower", cursive; font-size: 40px; }
  .name-band__name { font-family: "Delius", cursive; font-weight: 700; font-size: 38px; }
  .title__party { z-index: 2; }

  .photo--cocktails {
    position: absolute; left: 0; top: 393px; width: 100%; height: 354px;
    background: radial-gradient(ellipse at 45% 70%, var(--drink), #8e3a22 55%, #4a2412);
  }

  .card--back { left: 628px; top: 42px; width: 532px; height: 743px; }
  .event-date { position: absolute; left: 40px; top: 84px; font-family: "Pinyon Script", cursive; font-size: 50px; color: var(--wine); white-space: nowrap; }
  .event-detail { position: absolute; left: 42px; font-family: "Fredoka", sans-serif; font-weight: 600; font-size: 24px; color: var(--wine); }
  .event-detail--time { top: 163px; }
  .event-detail--rsvp { top: 240px; }
  .photo--cocktails-faded {
    position: absolute; left: 57px; top: 430px; width: 418px; height: 278px;
    background: radial-gradient(ellipse at 40% 60%, #e08a62, var(--glow) 70%, #f5c98a);
    opacity: 0.9;
  }
</style>
</head>
<body>
<main class="canvas">
  <div class="side-label side-label--front">
    <svg width="50" height="90" viewBox="0 0 50 90" aria-hidden="true"><path d="M13 0h24v48h13L25 90 0 48h13z" fill="var(--ink)"/></svg>
    <span>FRONT</span>
  </div>

  <section class="card card--front">
    <svg class="card__arc" viewBox="0 0 532 747" aria-hidden="true"><path d="M0 245 Q250 300 532 120 V0 H0Z" fill="#fff" opacity="0.12"/></svg>
    <div class="title title__age">50<sup>th</sup></div>
    <div class="title title__birthday">Birthday</div>
    <div class="name-band"><span class="name-band__for">for</span><span class="name-band__name">Tim</span></div>
    <div class="title title__party">Party</div>
    <div class="photo--cocktails" role="img" aria-label="Photo of rows of red cocktails in martini glasses"></div>
  </section>

  <section class="card card--back">
    <svg class="card__arc" viewBox="0 0 532 743" aria-hidden="true"><path d="M0 245 Q300 300 532 60 V0 H0Z" fill="#fff" opacity="0.12"/></svg>
    <div class="event-date">19th October, 2013</div>
    <div class="event-detail event-detail--time">7.00 P.M</div>
    <div class="event-detail event-detail--rsvp">RSVP: 14th October, 2013</div>
    <div class="photo--cocktails-faded" role="img" aria-label="Faded photo of red cocktails in martini glasses"></div>
  </section>

  <div class="side-label side-label--back">
    <svg width="50" height="90" viewBox="0 0 50 90" aria-hidden="true"><path d="M13 90h24V42h13L25 0 0 42h13z" fill="var(--ink)"/></svg>
    <span>BACK</span>
  </div>
</main>
</body>
</html>
```